Business Card Design and New Company Logo

I need a business card design and new company logo for a plant nursery. I will be propagating landscape plants from cuttings and growing them locally for resale, locally grown and nurtured plants for zone 5 climate. I would like a design that depicts the growth of shoots to roots .... locally grown and nurtured landscape plants. Healthy, hardy ornamental trees and shrubs for $4.97. Affordable gardening for all.
Updates
Hello Designers,
Thank you for your submissions. I am going to be out of my office until Monday. I will continue to review submitted designs when I can and posting requests for revisions when time permits on my business trip. I should have a decision next week.
Sincerely,
Marla
Sorry for my delay in choosing a design. I had some unforeseen business and personal events culminate at the same time. I will have my decision by the end of this week and update all by Friday March 21. Thank you for your design submissions and your patience.
Marla
Target Market(s)
Home owners
Industry/Entity Type
Landscape
Contact Information for Business Card
Fernbrook Hollow Nursery
Marla Dunwick
812 Calder Pond Lane
Wrenford, NH 03999
555-862-3094
Fernbrook4Hollow@mailvine.net
Look and feel
Each slider illustrates characteristics of the customer's brand and the style your logo design should communicate.

```html
<!DOCTYPE html>
<html lang="en">
<head>
<meta charset="utf-8">
<title>Fernbrook Hollow Nursery — Business Card</title>
<link rel="stylesheet" href="https://fonts.googleapis.com/css2?family=Open+Sans:wght@400;600;700&family=Satisfy&display=swap">
<style>
  :root {
    --backdrop: #9c9c9c;
    --card: #ffffff;
    --card-shade: #ececec;
    --leaf-green: #2f7a34;
    --ink-gray: #5e5d58;
  }
  html, body {
    margin: 0;
    width: 1200px;
    height: 900px;
    overflow: hidden;
    background: var(--backdrop);
  }
  .canvas {
    position: relative;
    width: 1200px;
    height: 900px;
    display: flex;
    align-items: center;
    justify-content: center;
  }
  .business-card {
    position: relative;
    width: 840px;
    height: 480px;
    background: radial-gradient(ellipse at 40% 30%, var(--card) 45%, var(--card-shade) 100%);
    box-shadow: 0 6px 18px rgba(0,0,0,0.25);
    font-family: "Open Sans", Arial, sans-serif;
    color: var(--ink-gray);
  }
  .brand {
    position: absolute;
    left: 70px;
    top: 70px;
    display: flex;
    align-items: center;
    gap: 18px;
  }
  .brand-dot {
    width: 30px;
    height: 30px;
    border-radius: 50%;
    background: var(--leaf-green);
  }
  .brand-name {
    font-family: "Open Sans", Arial, sans-serif;
    font-weight: 600;
    font-size: 46px;
    color: var(--leaf-green);
    letter-spacing: -0.5px;
    line-height: 1;
  }
  .contact-person {
    position: absolute;
    left: 70px;
    top: 262px;
  }
  .person-name {
    font-family: "Satisfy", cursive;
    font-size: 44px;
    color: var(--leaf-green);
    line-height: 1.1;
    margin: 0 0 8px;
    font-weight: 400;
  }
  .contact-line {
    font-size: 21px;
    line-height: 1.45;
    margin: 0;
  }
  .company-address {
    position: absolute;
    left: 460px;
    top: 318px;
    font-style: normal;
  }
  .company-name {
    font-weight: 700;
    font-size: 20px;
    margin: 0 0 2px;
  }
  .address-line {
    font-size: 20px;
    line-height: 1.45;
    margin: 0;
  }
</style>
</head>
<body>
  <main class="canvas">
    <section class="business-card">
      <div class="brand">
        <span class="brand-dot"></span>
        <span class="brand-name">Fernbrook Hollow Nursery</span>
      </div>

      <div class="contact-person">
        <h1 class="person-name">Marla Dunwick</h1>
        <p class="contact-line">555-862-3094</p>
        <p class="contact-line">Fernbrook4Hollow@mailvine.net</p>
      </div>

      <address class="company-address">
        <p class="company-name">Fernbrook Hollow Nursery</p>
        <p class="address-line">812 Calder Pond Lane Wrenford,</p>
        <p class="address-line">NH 03999</p>
      </address>
    </section>
  </main>
</body>
</html>
```